Bramwell Health Promotional flyer

Develop a professional flyer to be distributed to potential clients for consulting services.
Company name: Bramwell Health
see attachments for company logo and other bullet points . Bold items need to be on the flyer as written, other items can be tweaked/updated to sound more appealing.

```html
<!DOCTYPE html>
<html lang="en">
<head>
<meta charset="utf-8">
<title>Bramwell Health – Flyer</title>
<link rel="stylesheet" href="https://fonts.googleapis.com/css2?family=Open+Sans:wght@400;600;700&display=swap">
<style>
  :root {
    --page-bg: #d9d9d6;
    --paper: #e7dfd2;
    --brand-blue: #1457ad;
    --box-blue: #0d4ea6;
    --box-sheen: #3f78c2;
    --plus-red: #e3393a;
    --ink: #2e2e2e;
    --footer: #474747;
    --white: #ffffff;
  }
  * { box-sizing: border-box; margin: 0; padding: 0; }
  html, body {
    width: 1200px; height: 800px; overflow: hidden;
    background: var(--page-bg);
    font-family: "Open Sans", Arial, sans-serif;
  }
  .flyer {
    position: absolute; left: 300px; top: 12px;
    width: 600px; height: 776px;
    background: var(--paper);
    overflow: hidden;
    box-shadow: 0 4px 14px rgba(0,0,0,.18);
  }
  .hero-photo {
    position: absolute; left: 0; top: 0; width: 600px; height: 330px;
    background:
      radial-gradient(ellipse at 75% 35%, #e8c9b4 0%, rgba(232,201,180,0) 40%),
      radial-gradient(ellipse at 42% 60%, #d9b48a 0%, rgba(217,180,138,0) 38%),
      linear-gradient(100deg, #ece6dc 0%, #ded3c5 40%, #c9a99a 70%, #f1ede8 100%);
  }
  .brand {
    position: absolute; left: 34px; top: 44px;
    display: flex; align-items: center; gap: 10px;
  }
  .brand-mark { width: 30px; height: 30px; background: var(--brand-blue); }
  .brand-name {
    font-weight: 700; font-size: 25px; letter-spacing: 1px;
    color: var(--brand-blue); text-transform: uppercase;
  }
  .info-box {
    position: absolute; top: 312px; height: 238px;
    background: var(--box-blue); color: var(--white);
    padding: 12px 12px 10px 14px;
  }
  .info-box.services {
    left: 16px; width: 272px;
    background: linear-gradient(160deg, var(--box-blue) 0%, var(--box-blue) 45%, var(--box-sheen) 70%, var(--box-blue) 90%);
  }
  .info-box.reasons { left: 296px; width: 282px; }
  .info-box h2 { font-weight: 600; font-size: 15px; margin-bottom: 4px; }
  .info-box.services h2 { font-size: 17px; letter-spacing: .5px; }
  .point-list { list-style: none; }
  .point-list li {
    position: relative; padding-left: 20px;
    font-size: 10px; line-height: 11px; margin-bottom: 8px;
  }
  .point-list li.bold { font-weight: 700; }
  .point-list li::before {
    content: "+"; position: absolute; left: 0; top: -5px;
    color: var(--plus-red); font-size: 18px; font-weight: 700;
  }
  .box-note { font-size: 10px; line-height: 13px; margin-top: 6px; }
  .headshot {
    position: absolute; left: 16px; top: 562px; width: 136px; height: 146px;
    background: linear-gradient(180deg, #ece9e4 0%, #dcd6ce 55%, #f4f4f4 100%);
  }
  .bio { position: absolute; left: 162px; top: 560px; width: 424px; color: var(--ink); }
  .bio h3 { font-size: 11.5px; font-weight: 700; margin-bottom: 1px; }
  .bio p { font-size: 9.8px; line-height: 13.5px; }
  .contact-bar {
    position: absolute; left: 0; bottom: 0; width: 600px; height: 40px;
    background: var(--footer); color: var(--white);
    display: flex; align-items: center; justify-content: center;
    font-size: 10.5px; white-space: nowrap;
  }
  .contact-bar b { font-weight: 700; }
  .contact-bar .sep { margin: 0 6px; opacity: .8; }
</style>
</head>
<body>
  <main class="flyer">
    <div class="hero-photo" role="img" aria-label="Photo of a smiling doctor examining a young child's mouth with a medical light"></div>

    <div class="brand">
      <span class="brand-mark"></span>
      <span class="brand-name">Bramwell Health</span>
    </div>

    <section class="info-box services">
      <h2>SERVICES</h2>
      <ul class="point-list">
        <li class="bold">Retention of Emergency Medicine trained physician, Dr. Thomas R. Hale MD for consultation on work-related injuries, illnesses or testing requirements.</li>
        <li class="bold">Assist with occupational health risk management.</li>
        <li>Concierge level service and care at one of Dr. Hale's 4 urgent care clinics when needed.</li>
        <li>Assistance setting up onsite clinics/ medics.</li>
        <li>Access to onsite services such as , u/covid vaccination clinics, onsite drug and alcohol testing, educational sessions, etc.</li>
      </ul>
    </section>

    <section class="info-box reasons">
      <h2>Why retain Bramwell Health</h2>
      <ul class="point-list">
        <li class="bold">24/7 access to a Medical Director.</li>
        <li class="bold">Reduction in recordable work-related injuries.</li>
        <li class="bold">Concierge level service for your employees and managers</li>
        <li>Access to Bramwell Health's referral network of Imaging and Orthopedics and other providers</li>
      </ul>
      <p class="box-note">Job sites do not need to be in Ohio for<br>Dr. Hale to provide consultative services.</p>
    </section>

    <div class="headshot" role="img" aria-label="Portrait photo of Dr. Thomas R. Hale in a white coat"></div>

    <section class="bio">
      <h3>Dr. Thomas R. Hale M.D.</h3>
      <p>Dr. Hale grew up in Upper Fernwood, Ohio and graduated from St. Aldric Preparatory High School, Northfield State University and Lakeshore Medical College.</p>
      <p>Dr. Hale is Board Certified as a Diplomate of the National Board of Acute Care Medicine and is a Fellow in the National Academy of Acute Care Medicine.</p>
      <p>He practiced Emergency Medicine for 17 years at Brookmere Medical Center in Kessington Ohio.</p>
      <p>Dr. Hale has practiced Urgent Care and Occupational Health Medicine for the last 29 years. He and his wife of 39 years have 3 children and live in Upper Fernwood, Ohio.</p>
    </section>

    <footer class="contact-bar">
      Fernwood&nbsp;<b>(555) 318-2047</b><span class="sep">|</span>
      Oakridge&nbsp;<b>(555) 462-7153</b><span class="sep">|</span>
      Millbrook&nbsp;<b>(555) 239-6081</b><span class="sep">|</span>
      Ashby&nbsp;<b>(555) 647-3925</b>
    </footer>
  </main>
</body>
</html>
```